packing for cake and sweet

we need packing design for cake box.
I attached some nice packing from other shop like :
Vira and belmonte for examples.

I attached the logo.
you can make packing with any colors you choose.

box size :
length : 30 cm
Width : 30 cm
Height : 15 cm

this shops have very good design :
https://www.pembrooke.co.uk/hot-chocolate/discover-hot-chocolate/all-hot-chocolate

Industry/Entity Type

food

Font styles to use
Other font styles liked:
• same our logo already attached.

```html
<!DOCTYPE html>
<html lang="en">
<head>
<meta charset="utf-8">
<title>Corvelle Cake Box Dieline</title>
<link rel="stylesheet" href="https://fonts.googleapis.com/css2?family=Cinzel:wght@400&display=swap">
<style>
  :root {
    --backdrop: #c6c9cc;
    --navy: #2f3543;
    --paper: #f1f2f4;
    --gold: #e59a45;
    --gold-soft: #ecc79a;
  }
  html, body {
    margin: 0;
    padding: 0;
    width: 1111px;
    height: 1200px;
    overflow: hidden;
    background: var(--backdrop);
  }
  .canvas {
    position: relative;
    width: 1111px;
    height: 1200px;
    background: var(--backdrop);
  }
  .dieline {
    position: absolute;
    left: 0;
    top: 0;
    width: 1111px;
    height: 1200px;
  }
  .panel-navy { fill: var(--navy); }
  .panel-paper { fill: var(--paper); }
  .brand-name {
    font-family: "Cinzel", "Trajan Pro", serif;
    font-weight: 400;
    font-size: 27px;
    letter-spacing: 0.5px;
    fill: var(--gold);
  }
</style>
</head>
<body>
<main class="canvas">
  <svg class="dieline" viewBox="0 0 1111 1200" xmlns="http://www.w3.org/2000/svg" aria-label="Flat dieline of the Corvelle cake box">
    <defs>
      <linearGradient id="artwork-tone" x1="0" y1="0" x2="0" y2="1">
        <stop offset="0" stop-color="#f1f2f4"/>
        <stop offset="0.35" stop-color="#d9cbb8"/>
        <stop offset="0.6" stop-color="#2f3543"/>
        <stop offset="1" stop-color="#2f3543"/>
      </linearGradient>
      <linearGradient id="pattern-tone" x1="0" y1="0" x2="1" y2="1">
        <stop offset="0" stop-color="#eeeff2"/>
        <stop offset="0.5" stop-color="#e6e2dc"/>
        <stop offset="1" stop-color="#eeeff2"/>
      </linearGradient>
    </defs>

    <!-- Lid: glue strip and top panel -->
    <rect class="panel-paper lid-tuck" x="64.2" y="335" width="249" height="16.8"/>
    <rect class="panel-navy lid-top" x="64.2" y="351.8" width="249" height="248.4"/>
    <text class="brand-name" x="188.7" y="486" text-anchor="middle">Corvelle</text>

    <!-- Side band -->
    <rect class="panel-navy glue-tab" x="48" y="600.2" width="16.2" height="124.2"/>
    <rect class="artwork-side" x="64.2" y="600.2" width="249" height="124.2" fill="url(#artwork-tone)" role="img" aria-label="Abstract brush-stroke artwork in navy and gold with a dotted circle"/>

    <rect class="panel-navy side-front" x="313.2" y="600.2" width="248.4" height="124.2"/>
    <text class="brand-name" x="437.4" y="672" text-anchor="middle">Corvelle</text>

    <rect class="pattern-side" x="561.6" y="600.2" width="249" height="124.2" fill="url(#pattern-tone)" role="img" aria-label="Repeating doodle pattern of swirls, blobs and gold dots"/>

    <rect class="panel-navy side-back" x="810.6" y="600.2" width="249" height="124.2"/>
    <text class="brand-name" x="935.1" y="672" text-anchor="middle">Corvelle</text>

    <!-- Base panel and tuck -->
    <rect class="panel-navy base" x="561.6" y="724.4" width="249" height="124.8"/>
    <rect class="panel-paper base-tuck" x="561.6" y="849.2" width="249" height="16.2"/>

    <!-- Dust flaps -->
    <polygon class="panel-paper flap" points="313.2,517.6 513,517.6 541.2,571 561.6,590.2 561.6,600.2 313.2,600.2"/>
    <polygon class="panel-paper flap" points="313.2,724.4 561.6,724.4 561.6,734.6 541.2,752 513,807.8 313.2,807.8"/>
    <polygon class="panel-paper flap" points="810.6,600.2 810.6,590.2 829.8,574 858.6,517.6 1059.6,517.6 1059.6,600.2"/>
    <polygon class="panel-paper flap" points="810.6,724.4 1059.6,724.4 1059.6,807.8 858.6,807.8 829.8,752 810.6,734.6"/>
  </svg>
</main>
</body>
</html>
```